Business Card Design

Brambleton Energy, L.P. is an energy and lifecycle management firm that creates value in petroleum products through synergistic marketing, trading, recovery, logistics and beneficial reuse services.

Sell top-quality refinery feedstock, petroleum products and co-products on the spot and futures makets (energy trading)

Separate, reclaim and/or manufacture valuable products for beneficial reuse (environmental)
Updates

The tag line Understanding Solutions   Performance are three different concepts and need to be kept either spaced apart or separated in some way. Thanks. 

Target Market(s)

Refiners, Petroleum storage companies, energy marketers

Industry/Entity Type

Business

Contact Information for Business Card

Gwendolyn R. Hask
Principal
Brambleton Energy, L.P.
4817 Quillby St.
Houston, TX 77081
713-482-6619 phone
713-641-8854 fax
g.hask@brambletonenergy-example.com
www.brambletonenergy-example.com

Requirements
Must have
• Tagline outlined in matching orange -

Understanding Solutions Performance
Nice to have
• Coordinating typestyles

```html
<!DOCTYPE html>
<html lang="en">
<head>
<meta charset="utf-8">
<title>Brambleton Energy, L.P. – Business Card</title>
<link rel="stylesheet" href="https://fonts.googleapis.com/css2?family=Roboto:wght@400;700;900&display=swap">
<style>
  :root {
    --backdrop: #2b2b2b;
    --card-top: #b9e0f7;
    --card-bottom: #6fb3e6;
    --ink: #111417;
    --accent: #f15a24;
    --white: #ffffff;
  }
  * { box-sizing: border-box; margin: 0; padding: 0; }
  html, body {
    width: 1200px; height: 900px; overflow: hidden;
    background: var(--backdrop);
    font-family: "Roboto", Arial, sans-serif;
  }
  .business-card {
    position: absolute; left: 180px; top: 210px;
    width: 840px; height: 480px; overflow: hidden;
    background: linear-gradient(160deg, var(--card-top) 0%, var(--card-bottom) 100%);
    box-shadow: 0 18px 40px rgba(0,0,0,.55);
  }
  .corner-band { position: absolute; left: 0; top: 0; }
  .brand {
    position: absolute; left: 52px; top: 178px;
    display: flex; align-items: center; gap: 16px;
  }
  .brand-dot { width: 46px; height: 46px; border-radius: 50%; background: var(--ink); flex: none; }
  .brand-name {
    color: var(--ink); font-weight: 900; font-size: 40px;
    line-height: 1.02; letter-spacing: 2px; text-transform: uppercase;
  }
  .tagline {
    position: absolute; left: 58px; top: 292px;
    color: var(--accent); font-weight: 700; font-size: 17px;
    display: flex; gap: 12px; align-items: center;
  }
  .tagline .divider { width: 5px; height: 5px; border-radius: 50%; background: var(--accent); }
  .holder { position: absolute; left: 400px; top: 48px; }
  .holder-name { color: var(--ink); font-weight: 900; font-size: 24px; text-transform: uppercase; letter-spacing: .5px; }
  .holder-title { color: var(--white); font-weight: 700; font-size: 16px; margin-top: 2px; }
  .contact-list {
    position: absolute; left: 400px; top: 130px;
    display: grid; grid-template-columns: 92px auto; row-gap: 9px;
    font-size: 18px;
  }
  .contact-list dt { color: var(--accent); }
  .contact-list dd { color: var(--ink); }
  .company-address { position: absolute; left: 400px; top: 370px; font-weight: 700; font-size: 20px; }
  .company-name { color: var(--white); }
  .street { color: var(--ink); margin-top: 2px; }
</style>
</head>
<body>
  <article class="business-card">
    <svg class="corner-band" width="840" height="480" viewBox="0 0 840 480" aria-hidden="true">
      <polygon points="380,480 840,440 840,480" fill="var(--ink)"/>
    </svg>

    <div class="brand">
      <span class="brand-dot"></span>
      <div class="brand-name">Brambleton<br>Energy L.P.</div>
    </div>
    <div class="tagline">
      <span>Understanding</span><span class="divider"></span>
      <span>Solutions</span><span class="divider"></span>
      <span>Performance</span>
    </div>

    <header class="holder">
      <h1 class="holder-name">Gwendolyn R. Hask</h1>
      <p class="holder-title">Principal</p>
    </header>

    <dl class="contact-list">
      <dt>Phone:</dt><dd>713-482-6619</dd>
      <dt>Fax:</dt><dd>713-641-8854</dd>
      <dt>Email:</dt><dd>g.hask@brambletonenergy-example.com</dd>
      <dt>Website:</dt><dd>www.brambletonenergy-example.com</dd>
    </dl>

    <address class="company-address" style="font-style:normal">
      <div class="company-name">Brambleton Energy, L.P.</div>
      <div class="street">4817 Quillby St. Houston, TX 77081</div>
    </address>
  </article>
</body>
</html>
```